New Web Design Project

New Roofing Website homepage mockup

Complete design document here: https://files.plorvex.net/doc/7tQmZrA2kLwP9xVbN4cYhE3sJdF8gUoR6iKe1nTy/edit?usp=sharing
Updates

Number of Pages Required

1 page

Font styles to use
Sans Serif

```html
<!DOCTYPE html>
<html lang="en">
<head>
<meta charset="utf-8">
<title>Keystone Roofing</title>
<link rel="stylesheet" href="https://fonts.googleapis.com/css2?family=Open+Sans:ital,wght@0,400;0,600;0,700;1,400&family=Montserrat:wght@500&display=swap">
<style>
:root{
  --blue:#2aa3df;
  --sky:#6ec4e8;
  --ink:#1e2a3a;
  --slate:#4b5668;
  --dark:#232323;
  --footer:#2b2b2b;
  --text:#333;
  --muted:#555;
  --white:#fff;
  --star:#f5a623;
}
*{margin:0;padding:0;box-sizing:border-box}
html,body{width:1200px;height:3236px;overflow:hidden}
body{position:relative;font-family:"Open Sans",sans-serif;color:var(--text);background:#f6f6f6}
.abs{position:absolute}
section{position:absolute;left:0;width:1200px;overflow:hidden}

/* hero */
.hero{top:0;height:591px;background:linear-gradient(120deg,#1b2636 0%,#2f3d52 35%,#56687f 60%,#24334a 100%)}
.hero-photo{position:absolute;inset:0;background:radial-gradient(ellipse at 70% 30%,rgba(140,160,185,.35),transparent 60%),linear-gradient(180deg,rgba(10,20,35,.1),rgba(10,20,35,.5))}
.brand{left:41px;top:76px;display:flex;align-items:center;gap:8px}
.brand-mark{width:14px;height:14px;background:var(--blue)}
.brand-name{font-weight:700;font-size:19px;line-height:22px;color:var(--white);letter-spacing:.5px}
.brand-tag{left:42px;top:102px;font-size:6px;line-height:8px;color:#cfd8e3;letter-spacing:2px}
.nav{right:92px;top:21px;display:flex;gap:21px}
.nav a{color:var(--white);font-size:13px;font-weight:600;text-decoration:none}
.hero h1{left:54px;top:278px;font-weight:600;font-size:40px;color:var(--white);letter-spacing:.3px}
.hero p{left:55px;top:333px;width:520px;font-style:italic;font-size:15.5px;line-height:19px;color:var(--white)}
.btn{display:flex;align-items:center;justify-content:center;background:var(--blue);color:var(--white);font-weight:600}
.hero .btn{left:57px;top:449px;width:170px;height:37px;font-size:13px}
.estimate{left:746px;top:82px;width:366px;height:414px;background:rgba(25,30,38,.88)}
.estimate h2{position:absolute;left:33px;top:30px;font-size:22px;font-weight:700;color:var(--white)}
.field-label{position:absolute;left:33px;font-size:8px;line-height:9px;color:#b9c0c9;text-transform:uppercase}
.select{position:absolute;left:33px;width:300px;height:32px;border:1px solid #cfd3d8;color:var(--white);font-size:10px;padding:0 7px;display:flex;align-items:center;justify-content:space-between}
.select svg{width:10px;height:6px}
.slider-label{position:absolute;left:33px;top:272px;font-size:10px;font-weight:700;color:var(--white)}
.track{position:absolute;left:33px;top:298px;width:300px;height:5px;background:var(--white);border-radius:3px}
.knob{position:absolute;left:230px;top:286px;width:30px;height:30px;border-radius:50%;background:var(--blue);color:var(--white);font-size:7px;display:flex;align-items:center;justify-content:center;border:2px solid #8fd3f3}
.total-label{position:absolute;left:33px;top:332px;font-size:10px;font-weight:700;color:var(--white)}
.total{position:absolute;left:33px;top:346px;font-size:40px;font-weight:700;color:var(--white)}

/* services */
.services{top:591px;height:561px;background:#f6f6f6}
.section-title{position:absolute;left:0;width:1200px;text-align:center;font-size:27px;font-weight:400}
.services .section-title{top:42px;color:#444}
.rule{left:13px;top:83px;width:1171px;height:2px;background:#cfcfcf}
.card{position:absolute;top:90px;width:300px;height:450px;background:var(--white);box-shadow:0 1px 4px rgba(0,0,0,.15)}
.card-photo{height:268px}
.card h3{font-family:"Montserrat",sans-serif;font-weight:500;font-size:16.5px;margin:26px 0 0 26px;color:#222}
.card ul{margin:16px 0 0 44px;font-size:12px;line-height:21px;color:#333}
.card .more{margin:13px 0 0 26px;font-size:11px;color:var(--blue);font-weight:600}

/* roofs */
.roofs{top:1152px;height:689px;background:linear-gradient(160deg,#56617a,#4a5568 50%,#545f75)}
.roofs .section-title{top:22px;color:var(--white)}
.roof{position:absolute;width:304px;height:206px;box-shadow:0 2px 6px rgba(0,0,0,.35)}
.roof-name{position:absolute;width:304px;text-align:center;font-size:17px;font-weight:600;color:var(--white)}
.soon{background:rgba(60,66,78,.8);display:flex;align-items:center;justify-content:center;font-size:33px;color:#9aa2ad;box-shadow:none}

/* projects */
.projects{top:1841px;height:565px}
.tile{position:absolute}
.intro{left:0;top:0;width:384px;height:282px;background:var(--dark)}
.intro h2{position:absolute;left:34px;top:81px;font-size:32px;font-weight:400;color:var(--white)}
.intro .btn{position:absolute;left:109px;top:173px;width:154px;height:45px;font-size:22px;font-weight:400}
.feature{left:384px;top:0;width:396px;height:282px;background:linear-gradient(180deg,#6b7278,#4f5a52 60%,#3c4440)}
.feature::after{content:"";position:absolute;inset:0;background:rgba(30,35,40,.45)}
.feature h2{position:absolute;z-index:1;left:0;width:396px;text-align:center;top:81px;font-size:32px;font-weight:400;color:var(--white)}
.feature .read{position:absolute;z-index:1;left:106px;top:187px;width:162px;height:39px;background:rgba(200,205,210,.35);color:var(--blue);font-size:16px;display:flex;align-items:center;justify-content:center}

/* reviews */
.reviews{top:2406px;height:475px;background:linear-gradient(100deg,#4d5f78 0%,#7a5a48 45%,#a3502e 70%,#4a2a1e 100%)}
.reviews::before{content:"";position:absolute;inset:0;background:rgba(20,25,35,.25)}
.reviews h2{position:absolute;z-index:1;width:1200px;text-align:center;top:73px;font-size:36px;font-weight:400;color:var(--white)}
.reviews .sub{position:absolute;z-index:1;width:1200px;text-align:center;top:126px;font-size:15px;color:var(--white)}
.quote{position:absolute;z-index:1;left:207px;top:226px;width:786px;text-align:center;font-size:16.5px;line-height:19px;color:var(--white)}
.stars{position:absolute;z-index:1;left:200px;top:344px;display:flex;gap:12px}
.reviewer{position:absolute;z-index:1;left:875px;top:352px;font-size:15px;line-height:19px;color:var(--white)}
.arrow{position:absolute;z-index:1;top:260px}
.dots{position:absolute;z-index:1;left:568px;top:415px;display:flex;gap:12px}
.dots i{width:8px;height:8px;border-radius:50%;background:rgba(255,255,255,.6)}
.dots i:first-child{background:var(--white)}

/* contact */
.contact{top:2881px;height:278px;background:var(--sky)}
.contact h2{position:absolute;width:1200px;text-align:center;top:30px;font-size:31px;font-weight:400;color:var(--white)}
.info{position:absolute;top:165px;display:flex;gap:10px}
.info svg{width:40px;height:40px;flex:none}
.info h4{font-size:11px;font-weight:600;color:var(--white);margin-bottom:8px}
.info p{font-size:10px;line-height:16px;color:var(--white);font-weight:600}

.footer{top:3159px;height:77px;background:var(--footer)}
.footer p{position:absolute;width:1200px;text-align:center;top:42px;font-size:8px;color:#ccc}
</style>
</head>
<body>

<section class="hero">
  <div class="hero-photo" role="img" aria-label="Roofer installing dark tile roofing, seen close up"></div>
  <div class="abs brand"><span class="brand-mark"></span><span class="brand-name">KEYSTONE ROOFING</span></div>
  <div class="abs brand-tag">CRAFT · TRUST · DURABILITY</div>
  <nav class="abs nav"><a href="#">HOME</a><a href="#">ABOUT US</a><a href="#">SERVICES</a><a href="#">PORTFOLIO</a><a href="#">CONTACT US</a></nav>
  <h1 class="abs">BUILT RIGHT, BUILT TO LAST</h1>
  <p class="abs">After over a decade of general contracting, we continue to see a repetitive trend by the roof purchase process where homeowners are constantly left confused, nervous, and worried when they need a new roof. As one of the most important features of keeping your home safe, this is unacceptable. Keystone Roofing was created to break this trend.</p>
  <a class="abs btn">REQUEST SERVICE</a>

  <div class="abs estimate">
    <h2>INSTANT Estimate</h2>
    <span class="field-label" style="top:92px">Type of service</span>
    <div class="select" style="top:104px">Completely replace roof<svg viewBox="0 0 10 6"><path d="M1 1l4 4 4-4" stroke="#fff" fill="none"/></svg></div>
    <span class="field-label" style="top:149px">Location type</span>
    <div class="select" style="top:161px">Home/Residence<svg viewBox="0 0 10 6"><path d="M1 1l4 4 4-4" stroke="#fff" fill="none"/></svg></div>
    <span class="field-label" style="top:204px">Roofing material</span>
    <div class="select" style="top:216px">Tile<svg viewBox="0 0 10 6"><path d="M1 1l4 4 4-4" stroke="#fff" fill="none"/></svg></div>
    <span class="slider-label">APROXIMATE ROOF SIZE (ft2)</span>
    <div class="track"></div>
    <div class="knob">1400</div>
    <span class="total-label">TOTAL</span>
    <span class="total">$6,110.00</span>
  </div>
</section>

<section class="services">
  <h2 class="section-title">SERVICES</h2>
  <div class="abs rule"></div>
  <article class="card" style="left:118px">
    <div class="card-photo" role="img" aria-label="Worker inspecting metal roof beside brick chimney" style="background:linear-gradient(160deg,#9a5a44,#6d7b8c 55%,#a9b4c0)"></div>
    <h3>Roof Inspections</h3>
    <ul><li>Water stains on the ceiling</li><li>Damaged or broken panels</li><li>Missing or damaged shingles</li></ul>
    <p class="more">READ MORE &nbsp;&gt;</p>
  </article>
  <article class="card" style="left:442px">
    <div class="card-photo" role="img" aria-label="Stack of roof tiles being installed under a cloudy sky" style="background:linear-gradient(160deg,#a8b6c6,#5a4a48 50%,#8f8d8a)"></div>
    <h3>Installation and Maintenance</h3>
    <ul><li>Shingles and metal roof installation</li><li>Rain gutters and downspouts cleaning</li><li>Ice dam formation prevention</li></ul>
    <p class="more">READ MORE &nbsp;&gt;</p>
  </article>
  <article class="card" style="left:766px">
    <div class="card-photo" role="img" aria-label="Carpenter on timber roof framing at sunset" style="background:radial-gradient(circle at 55% 75%,#fff3c8,#e0a24a 35%,#7a6a7c 80%)"></div>
    <h3>Roof Replacement</h3>
    <ul><li>Ensure safety</li><li>Energy efficiency</li><li>Makes your home much easier to sell</li></ul>
    <p class="more">READ MORE &nbsp;&gt;</p>
  </article>
</section>

<section class="roofs">
  <h2 class="section-title">TYPES OF ROOFS</h2>
  <div class="roof" style="left:112px;top:99px;background:linear-gradient(160deg,#5c9be0 0%,#9cc4ea 25%,#b88d5a 45%,#8f6a3e)" role="img" aria-label="Cedar shake roof under blue sky"></div>
  <span class="roof-name" style="left:112px;top:320px">Cedar</span>
  <div class="roof" style="left:441px;top:99px;background:linear-gradient(160deg,#eef2f4,#4c5766 45%,#9aa4ae 75%,#e6e3dc)" role="img" aria-label="Standing seam metal roof on a house"></div>
  <span class="roof-name" style="left:441px;top:320px">Metal</span>
  <div class="roof" style="left:770px;top:99px;background:linear-gradient(150deg,#5b6672,#7a8896 50%,#4c5560)" role="img" aria-label="Slate tile roof close up"></div>
  <span class="roof-name" style="left:770px;top:320px">Slate</span>
  <div class="roof" style="left:112px;top:380px;background:linear-gradient(160deg,#c9d8e6,#55596a 40%,#4a4d5c 70%,#a2856c)" role="img" aria-label="Asphalt shingle roof on a brick house"></div>
  <span class="roof-name" style="left:112px;top:600px">Asphalt</span>
  <div class="roof" style="left:441px;top:380px;background:linear-gradient(160deg,#5d6b3d,#2a2c2e 40%,#9c5a44 70%,#e0dcd6)" role="img" aria-label="Flat rubber roof on a brick building"></div>
  <span class="roof-name" style="left:441px;top:600px">Rubber</span>
  <div class="roof soon" style="left:770px;top:378px">COMING SOON</div>
</section>

<section class="projects">
  <div class="tile intro"><h2>Our latest projects</h2><a class="btn">All projects</a></div>
  <div class="tile feature" role="img" aria-label="Grey shingled house in Lexington with driveway">
    <h2>Lexington, MA</h2><span class="read">READ MORE</span>
  </div>
  <div class="tile" style="left:780px;top:0;width:420px;height:282px;background:linear-gradient(180deg,#b9d1ea,#d6dde2 35%,#8a8f8e 55%,#4f8a3a 75%,#3f7a2c)" role="img" aria-label="Large grey colonial home with green lawn"></div>
  <div class="tile" style="left:0;top:282px;width:384px;height:283px;background:linear-gradient(180deg,#7aa9d8,#e6ecef 40%,#7d8287 70%,#2b2d30)" role="img" aria-label="White house with a company pickup truck in front"></div>
  <div class="tile" style="left:384px;top:282px;width:396px;height:283px;background:linear-gradient(160deg,#3f6b34,#5f6e62 45%,#9aa0a3 70%,#3a5a30)" role="img" aria-label="Aerial view of green house among trees"></div>
  <div class="tile" style="left:780px;top:282px;width:420px;height:283px;background:linear-gradient(180deg,#3e6a2e,#e9ecee 45%,#7f878c 60%,#5a9a3a)" role="img" aria-label="Aerial view of white house with patio and lawn"></div>
</section>

<section class="reviews" role="img" aria-label="Blurred terracotta roof tiles under sky">
  <h2>Customer experience</h2>
  <p class="sub">Save Time and Money with a Top-Rated Service</p>
  <svg class="arrow" style="left:128px" width="20" height="34" viewBox="0 0 20 34"><path d="M17 2L3 17l14 15" stroke="#fff" stroke-width="3" fill="none"/></svg>
  <svg class="arrow" style="left:1054px" width="20" height="34" viewBox="0 0 20 34"><path d="M3 2l14 15L3 32" stroke="#fff" stroke-width="3" fill="none"/></svg>
  <p class="quote">"We needed to put a new roof on our house, as well as repair a sagging porch roof. Shingles had been flying off and we had had several leaks. Dale provided a very reasonable estimate - well below some of the other HomeRate List companies. The work was done very promptly and professionally. A couple of issues that arose were settled to our satisfaction and Dale took full ownership of the situation. It was very clear that customer satisfaction is a priority for this company. I would definitely recommend and hire again."</p>
  <div class="stars">
    <svg width="13" height="13" viewBox="0 0 24 24"><path fill="#f5a623" d="M12 2l3 7h7l-5.6 4.3 2.1 7.2L12 16.3 5.5 20.5l2.1-7.2L2 9h7z"/></svg>
    <svg width="13" height="13" viewBox="0 0 24 24"><path fill="#f5a623" d="M12 2l3 7h7l-5.6 4.3 2.1 7.2L12 16.3 5.5 20.5l2.1-7.2L2 9h7z"/></svg>
    <svg width="13" height="13" viewBox="0 0 24 24"><path fill="#f5a623" d="M12 2l3 7h7l-5.6 4.3 2.1 7.2L12 16.3 5.5 20.5l2.1-7.2L2 9h7z"/></svg>
    <svg width="13" height="13" viewBox="0 0 24 24"><path fill="#f5a623" d="M12 2l3 7h7l-5.6 4.3 2.1 7.2L12 16.3 5.5 20.5l2.1-7.2L2 9h7z"/></svg>
    <svg width="13" height="13" viewBox="0 0 24 24"><path fill="#f5a623" d="M12 2l3 7h7l-5.6 4.3 2.1 7.2L12 16.3 5.5 20.5l2.1-7.2L2 9h7z"/></svg>
  </div>
  <p class="reviewer">MARTA GREELEY<br>Reviewer</p>
  <div class="dots"><i></i><i></i><i></i><i></i></div>
</section>

<section class="contact">
  <h2>LET'S WORK TOGETHER</h2>
  <div class="info" style="left:118px">
    <svg viewBox="0 0 40 40" fill="none" stroke="#333" stroke-width="2"><circle cx="22" cy="18" r="14"/><path d="M22 9v9l6 4"/><circle cx="10" cy="30" r="5" fill="#6ec4e8"/></svg>
    <div><h4>WORKING HOURS</h4><p>Mon - Sat 8.00 - 18.00<br>Sunday CLOSED</p></div>
  </div>
  <div class="info" style="left:366px">
    <svg viewBox="0 0 40 40" fill="none" stroke="#333" stroke-width="2"><path d="M20 36s-11-12-11-20a11 11 0 0 1 22 0c0 8-11 20-11 20z"/><circle cx="20" cy="16" r="4"/></svg>
    <div><h4>LOCATION</h4><p>48 Alder St.<br>Brookfield MA 01506</p></div>
  </div>
  <div class="info" style="left:614px">
    <svg viewBox="0 0 40 40" fill="none" stroke="#333" stroke-width="2"><rect x="12" y="3" width="16" height="34" rx="2"/><path d="M18 32h4"/></svg>
    <div><h4>CALL CENTAR</h4><p>555-014-2290</p></div>
  </div>
  <div class="info" style="left:864px">
    <svg viewBox="0 0 40 40" fill="none" stroke="#333" stroke-width="2"><path d="M4 18l32-10-12 26-6-10z"/><path d="M18 24L36 8"/></svg>
    <div><h4>WRITE US</h4><p>DaleMercer@KeystoneRoofingCo.com</p></div>
  </div>
</section>

<section class="footer"><p>Copyright © 2020 Keystone Roofing, All Right Reserved</p></section>

</body>
</html>
```